card design for engineering consultancy

engineering drafting and project management company the provides drafting services for.
Electrical, Hydraulic, Mechanical, and Civil services
The company is called Q7R Services and logo is as attached
Information on card should be.
1. Logo
2.website : Q7RServices.example
3. email : info@Q7RServices.example
4. Phone: (+61) 400512836
5. Motto: Design - Document - Develop - Deliver

this card should be basically used for business identification only

Target Market(s)

electricians plumbers air conditioning installers and civil contractors

Industry/Entity Type

engineering, drafting, electrical, plumbing, airconditioning, civil

Contact Information for Business Card

1. Logo 2.website : Q7RServices.example 3. email : info@Q7RServices.example 4. Phone: (+61) 400512836 5. Motto: Design - Document - Develop - Deliver

Font styles to use
Serif

Requirements
Must have
• logo
Nice to have
• something inovative and different that makes it stand out from being just another business card

```html
<!DOCTYPE html>
<html lang="en">
<head>
<meta charset="utf-8">
<title>Q7R Services — Business Card</title>
<link rel="stylesheet" href="https://fonts.googleapis.com/css2?family=Montserrat:wght@400;500;600;700&display=swap">
<style>
  :root {
    --backdrop: #d9d9d9;
    --card: #f8f8f7;
    --ink: #414143;
    --ink-soft: #4a4a4c;
    --accent: #d71f2b;
    --shadow: rgba(0,0,0,0.28);
  }
  * { margin: 0; padding: 0; box-sizing: border-box; }
  html, body { width: 1200px; height: 882px; overflow: hidden; }
  body {
    background: var(--backdrop);
    font-family: "Montserrat", sans-serif;
    color: var(--ink);
    position: relative;
  }
  .card {
    position: absolute;
    left: 347px;
    width: 506px;
    height: 288px;
    background: var(--card);
    box-shadow: 1px 2px 3px var(--shadow);
  }
  .card--front { top: 129px; }
  .card--back { top: 466px; }

  .wordmark {
    display: flex;
    align-items: center;
    gap: 10px;
    font-weight: 700;
    color: var(--ink);
    letter-spacing: 0.06em;
    text-transform: uppercase;
    white-space: nowrap;
  }
  .wordmark__square { background: var(--accent); flex: none; }

  .card--front .wordmark {
    position: absolute;
    left: 0; right: 0; top: 118px;
    justify-content: center;
    font-size: 34px;
  }
  .card--front .wordmark__square { width: 26px; height: 26px; }

  .card--back .wordmark {
    position: absolute;
    left: 48px; top: 130px;
    font-size: 19px;
  }
  .card--back .wordmark__square { width: 16px; height: 16px; }

  .divider {
    position: absolute;
    left: 252px; top: 96px;
    width: 1px; height: 94px;
    background: var(--accent);
  }
  .contact-block {
    position: absolute;
    left: 274px; top: 94px;
  }
  .person-name {
    font-size: 23px;
    font-weight: 600;
    color: var(--ink);
    line-height: 1.1;
  }
  .person-role {
    font-size: 12.5px;
    font-weight: 400;
    color: var(--accent);
    margin-top: 2px;
  }
  .contact-list {
    list-style: none;
    margin-top: 10px;
  }
  .contact-list li {
    display: flex;
    align-items: center;
    gap: 7px;
    font-size: 12px;
    color: var(--ink-soft);
    height: 17px;
  }
  .contact-list svg { width: 11px; height: 11px; flex: none; }

  .motto {
    position: absolute;
    left: 0; right: 0; bottom: 20px;
    text-align: center;
    font-size: 12.5px;
    color: var(--ink-soft);
  }
  .motto__dot { color: var(--accent); margin: 0 3px; }
</style>
</head>
<body>
  <section class="card card--front" aria-label="Card front">
    <div class="wordmark">
      <span class="wordmark__square"></span>
      <span>Q7R Services</span>
    </div>
  </section>

  <section class="card card--back" aria-label="Card back">
    <div class="wordmark">
      <span class="wordmark__square"></span>
      <span>Q7R Services</span>
    </div>

    <div class="divider"></div>

    <div class="contact-block">
      <h1 class="person-name">Marten Ozola</h1>
      <p class="person-role">Executive Director</p>
      <ul class="contact-list">
        <li>
          <svg viewBox="0 0 12 12" aria-hidden="true"><path d="M2.5 1 L4.5 1 L5.2 3.6 L3.9 4.6 Q5 7 7.4 8.1 L8.4 6.8 L11 7.5 L11 9.5 Q10.5 11 9 11 Q2.5 10 1 3 Q1 1.5 2.5 1 Z" fill="none" stroke="#d71f2b" stroke-width="1.2" stroke-linejoin="round"/></svg>
          <span>(+61) 400512836</span>
        </li>
        <li>
          <svg viewBox="0 0 12 12" aria-hidden="true"><rect x="0.5" y="2" width="11" height="8" fill="#d71f2b"/><path d="M1 2.5 L6 6.5 L11 2.5" fill="none" stroke="#fff" stroke-width="1"/></svg>
          <span>info@Q7RServices.example</span>
        </li>
        <li>
          <svg viewBox="0 0 12 12" aria-hidden="true"><circle cx="6" cy="6" r="5" fill="none" stroke="#d71f2b" stroke-width="1.1"/><ellipse cx="6" cy="6" rx="2.2" ry="5" fill="none" stroke="#d71f2b" stroke-width="1"/><path d="M1 6 H11 M2 3.5 H10 M2 8.5 H10" stroke="#d71f2b" stroke-width="0.9"/></svg>
          <span>www.Q7RServices.example</span>
        </li>
      </ul>
    </div>

    <p class="motto">Design<span class="motto__dot">•</span>Document<span class="motto__dot">•</span>Develop<span class="motto__dot">•</span>Deliver</p>
  </section>
</body>
</html>
```